Website Banner Design Needed for Health/Medical Business

We are looking for a creative and professional set of banners for the front page of our:
1. website - lumenworthclinic.com.au and velbrooktreat.com.au and tarnmoreplus.com.au

then edit the above banners to the corrrect sizes for below
2. Our facebook pages (1 for each of the above websites)

3. Our google + pages (2 in total one for melb and syd)

4. You tube pages (1 for lumenworthclinic and 1 for velbrooktreat)

We are looking for something fresh and clean that gives the feeling of:
1. Medical (dont show pictures of doctors though - nurses are ok - just not doctors)
2. Modern because PRP is a modern medical procedure
3. Most Experienced - No other clinic in Australia has performed as many PRP treatments compared to us.
4. We offer a 100% money back guarantee as well

The banners will not be animated or using layers. they will be still banners.

We would prefer to use new stock images and will purchase them for you after you have provided some suggestions/initial drafts.

Target Market(s)

men and women from 25-65

Industry/Entity Type

Health And Wellness

Number of Pages Required

1 page

Font styles to use
Sans Serif

Requirements
Must have
• no doctor images
• nurses are ok - but no doctor images
• for the images avoid fake themed images eg. a person looking in the mirror at their hair loss = NO NO NO..... instead aim for a nurse holding a test tube or a clipboard .
• The banners need to emphasise we are the only clinic who has performed 11,000+ treatments in australia
Nice to have
• a medical feeling would be nice - but dont make it too medical. i want the viewer to associate the word TRUSTED PROVEN and RELIABLE when they view the banner.
Should not have
• as mentioned no doctor or images that look like hospital too much.
• we are a private clinic run by nurses - i have to becareful not to mislead the viewer

```html
<!DOCTYPE html>
<html lang="en">
<head>
<meta charset="utf-8">
<title>PRP Hair Treatment Banner</title>
<link rel="stylesheet" href="https://fonts.googleapis.com/css2?family=Cormorant+Garamond:wght@600&family=Montserrat:wght@400;500;700&family=Pinyon+Script&display=swap">
<style>
  :root {
    --page-bg: #e9eaed;
    --navy: #1e3c78;
    --mid-blue: #2c5896;
    --sky-1: #c9d8e8;
    --sky-2: #e9f0f8;
    --sky-3: #f6f9fc;
    --band: rgba(255, 255, 255, 0.72);
    --green: #4cbf62;
    --white: #ffffff;
    --scrub: #57b9c7;
  }
  * { margin: 0; padding: 0; box-sizing: border-box; }
  html, body {
    width: 1200px; height: 675px; overflow: hidden;
    background: var(--page-bg);
  }
  .banner {
    position: absolute; left: 0; top: 96px;
    width: 1200px; height: 482px; overflow: hidden;
    background:
      radial-gradient(ellipse 420px 260px at 180px 90px, var(--sky-1), transparent 75%),
      radial-gradient(ellipse 500px 300px at 1000px 120px, var(--sky-2), transparent 80%),
      linear-gradient(180deg, var(--sky-2) 0%, var(--sky-3) 60%, var(--sky-2) 100%);
  }
  .info-band {
    position: absolute; left: 0; top: 235px; width: 600px; height: 108px;
    background: linear-gradient(90deg, var(--band) 0%, var(--band) 70%, rgba(255,255,255,0) 100%);
  }
  .headline {
    position: absolute; left: 69px; top: 126px;
    font-family: "Cormorant Garamond", serif; font-weight: 600;
    font-variant: small-caps; font-size: 54px; line-height: 46px;
    color: var(--navy); letter-spacing: 0.2px;
  }
  .claim {
    position: absolute; left: 69px; top: 250px;
    font-family: "Montserrat", sans-serif; color: var(--mid-blue);
  }
  .claim-lead { font-size: 27px; font-weight: 400; line-height: 34px; padding-left: 4px; }
  .claim-figure { font-size: 36px; font-weight: 700; color: var(--navy); line-height: 44px; }
  .features {
    position: absolute; left: 69px; top: 356px;
    display: flex; gap: 20px; align-items: center;
    font-family: "Pinyon Script", cursive; font-size: 23px; color: var(--navy);
  }
  .feature { display: flex; align-items: center; gap: 5px; }
  .feature svg { width: 14px; height: 14px; fill: var(--navy); }
  .nurse-photo {
    position: absolute; left: 569px; top: 0; width: 341px; height: 482px;
    background:
      radial-gradient(ellipse 60px 75px at 170px 85px, #d8a78c, transparent 100%),
      radial-gradient(ellipse 160px 220px at 170px 330px, var(--scrub), transparent 85%),
      linear-gradient(180deg, rgba(233,240,248,0) 0%, rgba(233,240,248,0) 100%);
  }
  .badge { position: absolute; left: 900px; top: 150px; width: 300px; height: 330px; }
</style>
</head>
<body>
  <section class="banner">
    <div class="info-band"></div>

    <h1 class="headline">Loosing Your Hair<br>is a Choice</h1>

    <div class="claim">
      <p class="claim-lead">Only Australian clinic to perform</p>
      <p class="claim-figure">11,000+ PRP Treatments</p>
    </div>

    <ul class="features">
      <li class="feature">
        <svg viewBox="0 0 16 16"><circle cx="8" cy="5" r="4"/><path d="M1 16c0-4 3-6 7-6s7 2 7 6z"/></svg>
        Trained Staff
      </li>
      <li class="feature">
        <svg viewBox="0 0 16 16"><path d="M2 1v5a4 4 0 0 0 8 0V1h-1.5v5a2.5 2.5 0 0 1-5 0V1zM6 10v1a4 4 0 0 0 8 0v-1h-1.5v1a2.5 2.5 0 0 1-5 0v-1z"/><circle cx="13.2" cy="8.5" r="1.8"/></svg>
        Reliable Equipment
      </li>
      <li class="feature">
        <svg viewBox="0 0 16 16"><path d="M8 0l7 3v5c0 4-3 7-7 8-4-1-7-4-7-8V3z"/></svg>
        Best Consultancy
      </li>
    </ul>

    <div class="nurse-photo" role="img" aria-label="Photo of a smiling nurse in teal scrubs holding a clipboard"></div>

    <svg class="badge" viewBox="0 0 300 330">
      <defs>
        <path id="badge-arc" d="M45 164 A118 118 0 0 1 262 98"/>
        <filter id="badge-shadow" x="-20%" y="-20%" width="140%" height="140%">
          <feDropShadow dx="0" dy="3" stdDeviation="4" flood-color="#1e3c78" flood-opacity="0.25"/>
        </filter>
      </defs>
      <text font-family="Pinyon Script, cursive" font-size="36" fill="#1e3c78">
        <textPath href="#badge-arc" startOffset="2%">Reliable &amp; Trusted</textPath>
      </text>
      <circle cx="163" cy="164" r="82" fill="#ffffff" filter="url(#badge-shadow)"/>
      <circle cx="163" cy="164" r="75" fill="#4cbf62"/>
      <text x="163" y="168" text-anchor="middle" font-family="Montserrat, sans-serif" font-weight="700" font-size="42" fill="#ffffff">100%</text>
      <text x="163" y="194" text-anchor="middle" font-family="Montserrat, sans-serif" font-weight="500" font-size="17" fill="#ffffff">Money Back</text>
      <text x="163" y="217" text-anchor="middle" font-family="Montserrat, sans-serif" font-weight="700" font-size="19" fill="#ffffff">Guarantee</text>
    </svg>
  </section>
</body>
</html>
```